Clerical Business Card Design

I have just started a new business focusing on Clerical / Administration Support for Small to Medium sized Businesses. I can provide support not just only my local area but anywhere as long as it is able to be done over the internet/email. I am the only person working in the business.
I would like to see some designs that are bright in colour yet a clean fresh design. The design should communicate balance.
Updates

Target Market(s)

Small to Medium sized Professional Businesses

Industry/Entity Type

Business

Contact Information for Business Card

Business Name: Vormley's Clerical
Statement: Providing Balanced Efficient Support
My Name: Ilsa Vormley
Phone: 0418 571 924 or 02 6519 4027
Email: vormleysclerical@plimmet.com.au

Colors

Designer to choose colors to be used in the design.

Requirements
Must have
• I'm open to suggestions
Nice to have
• I would like to see maybe something done with the two "C" in the business name whether that could be a focus of difference
Should not have
• Cartoon type pictures

```html
<!DOCTYPE html>
<html lang="en">
<head>
<meta charset="utf-8">
<title>Vormley's Clerical – Business Card</title>
<link rel="stylesheet" href="https://fonts.googleapis.com/css2?family=Rokkitt:wght@300;400&display=swap">
<style>
  :root {
    --backdrop: #9b9b9b;
    --paper: #ffffff;
    --leaf: #b5d672;
    --sage: #a9c193;
    --ink-light: #ffffff;
    --card-w: 960px;
    --card-h: 604px;
  }
  * { margin: 0; padding: 0; box-sizing: border-box; }
  html, body {
    width: 1200px;
    height: 1083px;
    overflow: hidden;
    background: var(--backdrop);
  }
  .business-card {
    position: absolute;
    left: 120px;
    top: 240px;
    width: var(--card-w);
    height: var(--card-h);
    background: var(--paper);
    overflow: hidden;
    font-family: "Rokkitt", Georgia, serif;
    font-weight: 300;
  }
  .card-shapes {
    position: absolute;
    inset: 0;
    width: 100%;
    height: 100%;
  }
  .brand {
    position: absolute;
    left: 40px;
    top: 168px;
    width: 280px;
    display: flex;
    flex-direction: column;
    align-items: flex-start;
    gap: 26px;
  }
  .brand-square {
    width: 150px;
    height: 150px;
    border: 8px solid var(--leaf);
  }
  .brand-name {
    font-size: 36px;
    line-height: 1;
    color: var(--leaf);
    white-space: nowrap;
    letter-spacing: 0.5px;
  }
  .holder-name {
    position: absolute;
    left: 404px;
    top: 160px;
    font-size: 82px;
    line-height: 1;
    color: var(--ink-light);
    white-space: nowrap;
  }
  .contact-line {
    position: absolute;
    color: var(--ink-light);
    white-space: nowrap;
    display: flex;
    align-items: center;
  }
  .contact-phones {
    left: 404px;
    top: 404px;
    font-size: 40px;
    line-height: 50px;
  }
  .phone-divider {
    display: inline-block;
    width: 3px;
    height: 72px;
    background: var(--ink-light);
    margin: 0 10px;
  }
  .contact-email {
    left: 384px;
    top: 494px;
    font-size: 35px;
    line-height: 46px;
  }
</style>
</head>
<body>
  <article class="business-card">
    <svg class="card-shapes" viewBox="0 0 960 604" aria-hidden="true">
      <path class="green-field" d="M322,0 Q462,302 322,604 L960,604 L960,0 Z" fill="var(--leaf)"/>
      <path class="divider-band" d="M300,0 Q440,302 300,604 L322,604 Q462,302 322,0 Z" fill="var(--sage)"/>

      <circle class="name-dot" cx="362" cy="209" r="38" fill="var(--paper)" stroke="var(--sage)" stroke-width="5"/>

      <g class="phone-badge">
        <circle cx="357" cy="429" r="37" fill="var(--paper)" stroke="var(--sage)" stroke-width="5"/>
        <path d="M345,407 l8,-3 l6,14 l-6,4 q3,10 11,17 l5,-5 l13,8 l-3,8 q-6,4 -14,0 q-20,-12 -26,-32 q-2,-8 6,-11 z" fill="var(--sage)"/>
      </g>

      <g class="mail-badge">
        <circle cx="336" cy="517" r="37" fill="var(--paper)" stroke="var(--sage)" stroke-width="5"/>
        <rect x="313" y="502" width="46" height="31" fill="var(--sage)"/>
        <path d="M313,503 L336,521 L359,503" fill="none" stroke="var(--paper)" stroke-width="3"/>
        <path d="M313,532 L330,516 M359,532 L342,516" fill="none" stroke="var(--paper)" stroke-width="2"/>
      </g>
    </svg>

    <div class="brand">
      <div class="brand-square"></div>
      <div class="brand-name">Vormley's Clerical</div>
    </div>

    <h1 class="holder-name">Ilsa Vormley</h1>

    <p class="contact-line contact-phones">
      <span class="phone-mobile">0418 571 924</span>
      <span class="phone-divider"></span>
      <span class="phone-office">02 6519 4027</span>
    </p>

    <p class="contact-line contact-email">vormleysclerical@plimmet.com.au</p>
  </article>
</body>
</html>
```